Business Card Design Project - IT Company

Kestrafield Information Technology Solutions
We are an Information Technology Company. We provide computer services to commercial companies. We would like a new card full color front and back with bleeding edge.
We have a logo that you can use or if you want to come up with a new logo that is fine too.
Our colors are mostly Maroon and black but be creative.
Sample Information
Brent R Okafor
4812 W Saguaro Ridge Drive
Suite 410
Chandler, AZ 85226
O: 602.914.2037
C: 602.468.1290
24/7: 888.914.2037
bokafor@kestrafield.example
www.kestrafield.example
Target Market(s)
Business of all sizes
Industry/Entity Type
Computer
Requirements
Must have
- Bleeding edge
full color on both sides

```html
<!DOCTYPE html>
<html lang="en">
<head>
<meta charset="utf-8">
<title>Kestrafield Business Card</title>
<link rel="stylesheet" href="https://fonts.googleapis.com/css2?family=Questrial&family=Michroma&display=swap">
<style>
  :root {
    --backdrop: #e7e8e9;
    --card-light: #ffffff;
    --card-shade: #dfe0e2;
    --maroon: #c1272d;
    --ink: #2b2b2b;
    --ink-soft: #555759;
    --mark-faint: #ead6d0;
  }
  * { box-sizing: border-box; margin: 0; padding: 0; }
  html, body { width: 1200px; height: 960px; overflow: hidden; }
  body {
    background: var(--backdrop);
    font-family: "Questrial", sans-serif;
    color: var(--ink);
    position: relative;
  }
  .card {
    position: absolute;
    width: 560px;
    height: 320px;
    background: radial-gradient(ellipse at 60% 45%, var(--card-light) 0%, #f1f2f3 45%, var(--card-shade) 100%);
    overflow: hidden;
  }
  .card--front { left: 60px; top: 90px; }
  .card--back { left: 580px; top: 550px; }

  .brand { position: absolute; display: flex; flex-direction: column; }
  .brand__row { display: flex; align-items: center; gap: 8px; }
  .brand__square { background: var(--maroon); display: block; }
  .brand__name { color: var(--ink); line-height: 1; }
  .brand__tagline { font-family: "Michroma", sans-serif; color: var(--ink); letter-spacing: 0.02em; white-space: nowrap; }

  .card--front .brand { left: 28px; top: 34px; }
  .card--front .brand__square { width: 26px; height: 26px; }
  .card--front .brand__name { font-size: 34px; }
  .card--front .brand__tagline { font-size: 6.4px; margin-top: 4px; }

  .address {
    position: absolute; right: 26px; top: 26px;
    font-style: normal;
    font-size: 11px; line-height: 1.3; color: var(--ink-soft); letter-spacing: 0.04em;
  }
  .rule { position: absolute; height: 1.5px; background: var(--maroon); }
  .rule--top { left: 210px; right: 38px; top: 110px; }
  .rule--bottom { left: 150px; right: 110px; top: 166px; }
  .person {
    position: absolute; left: 0; right: 0; top: 120px;
    text-align: center; font-size: 30px; line-height: 36px; letter-spacing: 0.03em; color: var(--ink);
  }
  .contacts {
    position: absolute; left: 220px; top: 176px;
    list-style: none; font-size: 11.5px; letter-spacing: 0.06em; color: var(--ink-soft);
  }
  .contacts li { display: flex; align-items: center; gap: 8px; height: 15px; }
  .contacts svg { width: 11px; height: 11px; flex: none; }
  .contacts .spacer { width: 11px; flex: none; }

  .band { position: absolute; left: 0; bottom: 0; width: 100%; height: 62px; }

  .card--back .brand { left: 40px; top: 30px; }
  .card--back .brand__square { width: 52px; height: 52px; }
  .card--back .brand__name { font-size: 60px; }
  .card--back .brand__tagline { font-size: 11.5px; margin-top: 8px; }
  .web {
    position: absolute; left: 54px; top: 226px;
    font-family: "Michroma", sans-serif; font-size: 13px; letter-spacing: 0.06em; color: var(--ink);
  }
  .faint-square {
    position: absolute; right: 30px; top: 130px;
    width: 140px; height: 140px; border-radius: 10px; background: var(--mark-faint); opacity: 0.8;
  }
</style>
</head>
<body>
<svg width="0" height="0" style="position:absolute" aria-hidden="true">
  <defs>
    <linearGradient id="band-fade" x1="0" y1="0" x2="1" y2="0">
      <stop offset="0" stop-color="#c1272d" stop-opacity="0.15"/>
      <stop offset="0.35" stop-color="#c1272d" stop-opacity="0.95"/>
      <stop offset="0.7" stop-color="#c1272d" stop-opacity="0.75"/>
      <stop offset="1" stop-color="#c1272d" stop-opacity="0.1"/>
    </linearGradient>
    <g id="stripes">
      <rect x="0" y="6" width="560" height="1.2" fill="url(#band-fade)" opacity="0.5"/>
      <rect x="0" y="14" width="560" height="2" fill="url(#band-fade)" opacity="0.7"/>
      <rect x="0" y="22" width="560" height="3" fill="url(#band-fade)"/>
      <rect x="0" y="29" width="560" height="4" fill="url(#band-fade)"/>
      <rect x="0" y="36" width="560" height="2.5" fill="url(#band-fade)" opacity="0.85"/>
      <rect x="0" y="43" width="560" height="3" fill="url(#band-fade)" opacity="0.7"/>
      <rect x="0" y="51" width="560" height="1.5" fill="url(#band-fade)" opacity="0.5"/>
      <rect x="0" y="58" width="560" height="2" fill="url(#band-fade)" opacity="0.35"/>
      <rect x="0" y="65" width="560" height="1" fill="url(#band-fade)" opacity="0.25"/>
    </g>
  </defs>
</svg>

<section class="card card--front" aria-label="Card front">
  <div class="brand">
    <div class="brand__row">
      <span class="brand__square"></span>
      <span class="brand__name">Kestrafield</span>
    </div>
    <span class="brand__tagline">INFORMATION TECHNOLOGY SOLUTIONS</span>
  </div>
  <address class="address">
    4812 W Saguaro Ridge Drive<br>
    Suite 410<br>
    Chandler, AZ 85226
  </address>
  <div class="rule rule--top"></div>
  <p class="person">Brent R Okafor</p>
  <div class="rule rule--bottom"></div>
  <ul class="contacts">
    <li>
      <svg viewBox="0 0 12 12"><circle cx="6" cy="6" r="5.3" fill="none" stroke="#555759" stroke-width="1"/><path d="M4 3.3l1 1.2-.6.8c.4.9 1 1.5 1.9 1.9l.8-.6 1.2 1-.6 1C5.6 8.4 3.6 6.4 3.4 4z" fill="#555759"/></svg>
      602.914.2037
    </li>
    <li><span class="spacer"></span>602.468.1290</li>
    <li>
      <svg viewBox="0 0 12 12"><circle cx="6" cy="6" r="5.3" fill="none" stroke="#555759" stroke-width="1"/><text x="6" y="7.6" font-size="4" text-anchor="middle" fill="#555759" font-family="sans-serif">24/7</text></svg>
      888.914.2037
    </li>
    <li>
      <svg viewBox="0 0 12 12"><circle cx="6" cy="6" r="5.3" fill="none" stroke="#555759" stroke-width="1"/><rect x="3.3" y="4.2" width="5.4" height="3.8" fill="none" stroke="#555759" stroke-width="0.8"/><path d="M3.3 4.2L6 6.3l2.7-2.1" fill="none" stroke="#555759" stroke-width="0.8"/></svg>
      bokafor@kestrafield.example
    </li>
  </ul>
  <svg class="band" viewBox="0 0 560 72" preserveAspectRatio="none" aria-hidden="true"><use href="#stripes"/></svg>
</section>

<section class="card card--back" aria-label="Card back">
  <div class="brand">
    <div class="brand__row">
      <span class="brand__square"></span>
      <span class="brand__name">Kestrafield</span>
    </div>
    <span class="brand__tagline">INFORMATION TECHNOLOGY SOLUTIONS</span>
  </div>
  <div class="faint-square" aria-hidden="true"></div>
  <p class="web">WWW.KESTRAFIELD.EXAMPLE</p>
  <svg class="band" viewBox="0 0 560 72" preserveAspectRatio="none" aria-hidden="true"><use href="#stripes"/></svg>
</section>
</body>
</html>
```